Fun but professional website required for school teaching consultancy.

Dear Designers,

I have an interesting brief for you. My client is a skilled teacher who is looking to promote her consultancy that provides bespoke training and support to other teachers.

She would like a website that promotes her philosophy for working with children, which is essentially that she wants to create a fun and creative learning environment for them, whilst maintaining the professionalism that is also required to succeed. Representation of the balance between these two points is crucial to the design.

Typically these kind of websites are pretty boring so we need something fun and vibrant, not uninviting ie those typical images of a teacher sat behind a desk or anything overly formal.

Here is an example of what we do not want: http://www.brightmarlowtutors.co.uk/ - in this one although my client liked the layout, she hated the graphics.

Here is a website that she really liked and captured the vibe of what she is trying to promote about herself: http://www.pennyvalekidsplace.com/ - this design indicates fun with learning, happy kids, lively colours and still has a professional feel as well.

If you have any further questions, please ask

Many thanks,

Gareth

PS Enclosed please find a whole bunch of resources (including site map) for this project. My client has supplied graphics, page content and plenty of visuals so hopefully this will make things easier
Updates

To all designers,

Thanks all your designs. Just to let you all know they have been sent to the client and I will supply feedback to you all individually when I get it.

Many thanks,
Gareth

Hi all,

We've had loads of designs for this project so thanks to you all very much. If there is any feedback to pass on, I will do this directly. Right now, all designs have been liked and are in the running. My client is going through them all and will make a decision on the deadline date which is the 10th May.
If you don't hear from me before then, it's simply because no alterations have been requested.

Many thanks.
Gareth

Industry/Entity Type

Training

```html
<!DOCTYPE html>
<html lang="en">
<head>
<meta charset="utf-8">
<title>Brightpath Consultancy</title>
<link rel="stylesheet" href="https://fonts.googleapis.com/css2?family=Open+Sans:wght@400;600&family=Ubuntu:wght@300;400;500&display=swap">
<style>
:root{
  --blue-top:#6aa8d8;
  --blue-bottom:#3b7cbd;
  --brand-blue:#3a7fc0;
  --link-blue:#1d5fa8;
  --text:#555;
  --maroon:#8c1f14;
  --orange:#f26a00;
  --footer-bg:#f4f4f4;
}
*{box-sizing:border-box;margin:0;padding:0}
html,body{width:1035px;height:1200px;overflow:hidden;background:#fff}
body{position:relative;font-family:"Open Sans",sans-serif;color:var(--text)}
.site-header{position:absolute;left:0;top:0;width:1035px;height:169px;background:linear-gradient(180deg,var(--blue-top),var(--blue-bottom))}
.brand{position:absolute;left:84px;top:98px;display:flex;align-items:center;gap:10px;color:#fff;font-family:"Ubuntu",sans-serif;font-weight:500;font-size:19px;letter-spacing:1.6px}
.brand-dot{width:16px;height:16px;border-radius:50%;background:#fff}
.contact{position:absolute;right:80px;top:66px;text-align:right;color:#fff}
.contact .call{font-size:14px}
.contact .phone{font-size:23px;line-height:28px}
.contact .email{font-size:11px;color:#123c6a;margin-top:3px;margin-right:-9px}
.main-nav{position:absolute;left:80px;top:143px;width:875px;height:50px;display:flex;box-shadow:0 2px 3px rgba(0,0,0,.15)}
.main-nav a{display:flex;align-items:center;justify-content:center;color:#fff;text-decoration:none;font-family:"Ubuntu",sans-serif;font-weight:500;font-size:15.5px;height:100%}
.nav-home{width:87px;background:linear-gradient(#ffb300,#ff8a00)}
.nav-courses{width:81px;background:linear-gradient(#9dd14a,#79b42a)}
.nav-biopics{width:168px;background:linear-gradient(#b53b30,#972920)}
.nav-yoga{width:63px;background:linear-gradient(#62cfee,#3cb5d9)}
.nav-pe{width:109px;background:linear-gradient(#6b2099,#53157f)}
.nav-tl{width:124px;background:linear-gradient(#ffa200,#ff8400)}
.nav-resources{width:99px;background:linear-gradient(#9dd14a,#79b42a)}
.nav-member{width:144px;background:linear-gradient(#b53b30,#972920)}
.hero{position:absolute;left:80px;top:205px;width:590px;height:305px;background:linear-gradient(135deg,#6f8a3a,#b9a27c 45%,#e7d9c8 75%,#8da45a)}
.hero-control{position:absolute;right:0;bottom:0;width:43px;height:33px;background:var(--brand-blue);display:flex;align-items:center;justify-content:center}
.blog{position:absolute;left:677px;top:205px;width:278px;height:307px;background:linear-gradient(180deg,#9ccb2e,#74a515);color:#fff;border-radius:2px}
.blog h2{font-family:"Ubuntu",sans-serif;font-weight:400;font-size:22px;height:52px;line-height:52px;padding-left:25px;background:rgba(0,0,0,.06)}
.blog-list{list-style:none;padding:0 18px 0 25px;margin-top:14px}
.blog-list li{padding:0 0 10px;border-bottom:1px solid rgba(255,255,255,.35)}
.blog-list li + li{padding-top:8px}
.blog-list li:last-child{border-bottom:0}
.blog-list h3{font-size:12px;font-weight:600;line-height:16px}
.blog-list p{font-size:9.5px;line-height:15.5px;margin-top:2px}
.blog-more{position:absolute;left:29px;top:272px;font-size:10.5px;color:#2d4a08;font-weight:600;display:flex;align-items:center;gap:5px}
.content h1,.content h2,.content p{position:absolute;left:82px;width:585px}
.content h1{top:530px;font-family:"Ubuntu",sans-serif;font-weight:400;font-size:29px;color:var(--brand-blue)}
.lead{top:572px;font-family:"Ubuntu",sans-serif;font-weight:300;font-size:13px;line-height:19px;color:var(--link-blue)}
.body{font-family:"Ubuntu",sans-serif;font-weight:300;font-size:11.2px;line-height:19px;color:#555}
.intro{top:618px}
.content h2{font-family:"Ubuntu",sans-serif;font-weight:400;font-size:16px}
.what{top:708px;color:var(--maroon)}
.what-text{top:733px}
.philosophy{top:892px;color:var(--orange)}
.philosophy-text{top:916px}
.partner-text{top:1004px}
.feature{position:absolute;left:677px;width:278px;height:158px;overflow:hidden}
.feature .photo{position:absolute;inset:0}
.feature .label{position:absolute;left:0;bottom:0;width:100%;height:48px;display:flex;align-items:center;padding-left:16px;color:#fff;font-family:"Ubuntu",sans-serif;font-weight:500;font-size:19px}
.feature .arrow{position:absolute;right:0;bottom:0;width:30px;height:48px;display:flex;align-items:center;justify-content:center;background:rgba(0,0,0,.1)}
.f-win{top:535px}.f-win .photo{background:linear-gradient(135deg,#7fa7b8,#e2c19d 50%,#5d8bb0)}.f-win .label{background:rgba(40,170,200,.85)}
.f-yoga{top:700px}.f-yoga .photo{background:linear-gradient(135deg,#c89a6a,#7d6fa6 50%,#d8a56e)}.f-yoga .label{background:rgba(255,160,0,.85)}
.f-sport{top:876px}.f-sport .photo{background:linear-gradient(135deg,#3a58b8,#e9c33c 50%,#2c7fd4)}.f-sport .label{background:rgba(110,30,160,.88)}
.site-footer{position:absolute;left:0;top:1095px;width:1035px;height:105px;background:var(--footer-bg);border-top:1px solid #e2e2e2}
.footer-nav{position:absolute;left:80px;top:25px;font-size:13px;color:#555}
.footer-nav span{margin:0 5px;color:#777}
.copyright{position:absolute;left:80px;top:56px;font-size:11px;color:#555}
.social{position:absolute;right:89px;top:24px;display:flex;gap:8px}
.social i{display:block;width:19px;height:19px;border-radius:2px}
.s1{background:#3b5998}.s2{background:#4fb4e8}.s3{background:#1a73a8}
</style>
</head>
<body>
<header class="site-header">
  <div class="brand"><span class="brand-dot"></span>BRIGHTPATH CONSULTANCY</div>
  <div class="contact">
    <div class="call">Call Us Now</div>
    <div class="phone">07700 900418</div>
    <div class="email">hello@brightpathconsultancy.co.uk</div>
  </div>
</header>
<nav class="main-nav">
  <a class="nav-home">Home</a><a class="nav-courses">Courses</a><a class="nav-biopics">Consultant Biopics</a><a class="nav-yoga">Yoga</a><a class="nav-pe">PE Services</a><a class="nav-tl">T &amp; L Services</a><a class="nav-resources">Resources</a><a class="nav-member">Member Only</a>
</nav>
<div class="hero" role="img" aria-label="Photo of three children examining a leaf outdoors">
  <div class="hero-control"><svg width="24" height="14" viewBox="0 0 24 14"><path d="M8 1 2 7l6 6M16 1l6 6-6 6" fill="none" stroke="#fff" stroke-width="2"/></svg></div>
</div>
<aside class="blog">
  <h2>Recent Blog Post</h2>
  <ul class="blog-list">
    <li><h3>Etiam eu urna Sed porta</h3><p>Suspendisse quam leo molestie sed luctus quis feugiat in pede Fusce tellus</p></li>
    <li><h3>Maecenas justo velit placerat</h3><p>Duis quam Nam eget lacus Aliquam erat volutpat Quisque dignissim congue leo</p></li>
    <li><h3>Maecenas justo velit placerat</h3><p>Duis quam Nam eget lacus Aliquam erat volutpat Quisque dignissim congue leo</p></li>
  </ul>
  <div class="blog-more">VIEW MORE BLOG <svg width="5" height="9" viewBox="0 0 5 9"><path d="M1 1l3 3.5L1 8" fill="none" stroke="#2d4a08" stroke-width="1.3"/></svg></div>
</aside>
<main class="content">
  <h1>Welcome to Brightpath Consultancy</h1>
  <p class="lead">Maecenas at justo id velit placerat molestie Donec dictum lectus non odio Cras a ante vitae enim iaculis aliquam Mauris nunc quam venenatis nec euismod</p>
  <p class="body intro">Pellentesque habitant morbi tristique senectus et netus et malesuada fames ac turpis egestas Cras id elit Integer quis urna Ut ante enim dapibus malesuada fringilla eu condimentum quis tellus Aenean porttitor eros vel dolor Donec convallis pede venenatis nibh</p>
  <h2 class="what">What We Do</h2>
  <p class="body what-text">Brightpath Consultancy specialises in providing bespoke Teaching and Learning and Physical Education support to the primary education sector. We offer a range of training and support methods, including team teaching, INSET, courses, coaching, mentoring, staff meetings and so on. Working with a diverse range of clients, such as individual primary and secondary schools, clusters, Northvale County Council, School Sports Partnerships, collaborations and Sports Coaches, we are committed to providing professional development that has a real impact on school improvement. Our consultants all bring with them a raft of experience in Primary Education, Physical Education and School Improvement, plus the skills to inspire and enthuse teachers.</p>
  <h2 class="philosophy">Our Philosophy</h2>
  <p class="body philosophy-text">We are passionate about teaching and learning – both ours and yours! We strive to practice what we preach and ensure that all our training and support is personalised for the group or individual that it is created for. We also know that our support is only as good as our own understanding, so we are dedicated to ensuring our own professional development and constantly reviewing and developing our practice.</p>
  <p class="body partner-text">We work in partnership with our clients to design bespoke professional development opportunities, constantly reviewing and developing the support with the client to ensure their requirements are met.</p>
</main>
<a class="feature f-win"><div class="photo" role="img" aria-label="Photo of cheering children at a sports event"></div><div class="label">Children Winning</div><div class="arrow"><svg width="10" height="20" viewBox="0 0 10 20"><path d="M1 1l8 9-8 9" fill="none" stroke="#fff" stroke-width="1.6"/></svg></div></a>
<a class="feature f-yoga"><div class="photo" role="img" aria-label="Photo of a group lying in a circle on a yoga floor"></div><div class="label">Yoga &amp; Excercise</div><div class="arrow"><svg width="10" height="20" viewBox="0 0 10 20"><path d="M1 1l8 9-8 9" fill="none" stroke="#fff" stroke-width="1.6"/></svg></div></a>
<a class="feature f-sport"><div class="photo" role="img" aria-label="Photo of a child crawling under a net on an inflatable course"></div><div class="label">Sports Activities</div><div class="arrow"><svg width="10" height="20" viewBox="0 0 10 20"><path d="M1 1l8 9-8 9" fill="none" stroke="#fff" stroke-width="1.6"/></svg></div></a>
<footer class="site-footer">
  <div class="footer-nav">Home<span>|</span>Courses<span>|</span>Consultant Biopics<span>|</span>Yoga<span>|</span>PE Services<span>|</span>T &amp; L Services<span>|</span>Resources<span>|</span>Member Only</div>
  <div class="copyright">© 2014 Company Name&nbsp; All right reserved&nbsp; Term of Use</div>
  <div class="social"><i class="s1"></i><i class="s2"></i><i class="s3"></i></div>
</footer>
</body>
</html>
```